Need creative website for award-winning author

I need someone to create a cool website for indie award-winning author Lorna Quibb. Right now she one young adult novel and a published short story. The site should appeal to both adults and children. The site has to needs to be available through PEXLOFT's platform.

HOME Page
About Lorna
Bio
Books
Community Projects
Appearances
Blogs & Videos
Contact
Store

Check out the following author's websites:
Mark Tilden
Sarah Kwell
Hazel Brnok
Dale Fenwright
Rick Abernath

Target Market(s)

Readers (all ages)

Industry/Entity Type

Adult

Coding

Coded - Design and coding required

Number of Pages Required

5+ page

Requirements
Must have
• Cutting edge look

```html
<!DOCTYPE html>
<html lang="en">
<head>
<meta charset="utf-8">
<title>Lorna Quibb — Author</title>
<link rel="stylesheet" href="https://fonts.googleapis.com/css2?family=Montserrat:wght@400;500;600&family=Raleway:wght@400;500&display=swap">
<style>
  :root {
    --white: #ffffff;
    --coral: #ec6a6a;
    --hero-dark: #231c22;
    --accent-red: #e0202e;
    --brand-pink: #e0175a;
    --button-top: #e8173b;
    --button-bottom: #e3157a;
    --footer-bg: #f4f4f4;
    --footer-text: #9a9a9a;
    --divider: #eeeeee;
    --totop-bg: #333333;
  }
  * { box-sizing: border-box; margin: 0; padding: 0; }
  html, body { width: 1200px; height: 1200px; overflow: hidden; background: var(--white); }
  body { position: relative; font-family: "Montserrat", sans-serif; }

  .book-strip { position: absolute; top: 0; left: 0; width: 1200px; height: 94px; border-bottom: 1px solid var(--divider); }
  .book-cover {
    position: absolute; top: 0; width: 223px; height: 94px;
    background: linear-gradient(160deg, #4fc3e8 0%, #2b7fd0 55%, #3a4fb0 100%);
  }

  .view-all-band {
    position: absolute; top: 212px; left: 0; width: 1200px; height: 146px;
    background: var(--coral);
    display: flex; align-items: center; justify-content: center;
  }
  .view-all-band span { color: var(--white); font-size: 16px; font-weight: 500; letter-spacing: 2.6px; }

  .hero {
    position: absolute; top: 358px; left: 0; width: 1200px; height: 570px;
    background: linear-gradient(180deg, #3a3236 0%, var(--hero-dark) 50%, #2a1a22 100%);
  }
  .hero-title {
    position: absolute; top: 496px; left: 0; width: 1200px; text-align: center;
    color: var(--white); font-size: 32px; font-weight: 500; letter-spacing: 1px;
  }
  .hero-rule { position: absolute; top: 571px; left: 512px; width: 180px; height: 2px; background: var(--accent-red); }
  .hero-text {
    position: absolute; top: 610px; left: 200px; width: 800px; text-align: center;
    color: var(--white); font-family: "Raleway", sans-serif; font-size: 22px; line-height: 33px;
  }
  .buy-button {
    position: absolute; top: 718px; left: 536px; width: 130px; height: 39px;
    background: linear-gradient(180deg, var(--button-top), var(--button-bottom));
    color: var(--white); font-size: 13.5px; font-weight: 500; letter-spacing: 1.6px;
    display: flex; align-items: center; justify-content: center;
  }

  .brand-bar { position: absolute; top: 928px; left: 0; width: 1200px; height: 136px; display: flex; align-items: center; justify-content: center; }
  .brand-name { color: var(--brand-pink); font-size: 40px; font-weight: 600; }

  .site-footer { position: absolute; top: 1064px; left: 0; width: 1200px; height: 136px; background: var(--footer-bg); }
  .copyright {
    position: absolute; top: 28px; left: 0; width: 1200px; text-align: center;
    color: var(--footer-text); font-size: 10px; letter-spacing: 0.8px;
  }
  .social-links { position: absolute; top: 69px; left: 531px; display: flex; gap: 10px; }
  .social-links span { width: 40px; height: 40px; border-radius: 50%; background: var(--white); display: block; }
  .back-to-top {
    position: absolute; top: 1170px; left: 1141px; width: 43px; height: 30px;
    background: var(--totop-bg); border-radius: 3px 3px 0 0;
    display: flex; align-items: center; justify-content: center;
  }
</style>
</head>
<body>
  <section class="book-strip">
    <div class="book-cover" style="left:110px" role="img" aria-label="Book cover artwork with underwater scene"></div>
    <div class="book-cover" style="left:364px" role="img" aria-label="Book cover artwork with underwater scene"></div>
    <div class="book-cover" style="left:618px" role="img" aria-label="Book cover artwork with underwater scene"></div>
    <div class="book-cover" style="left:871px" role="img" aria-label="Book cover artwork with underwater scene"></div>
  </section>

  <section class="view-all-band"><span>VIEW ALL BOOKS</span></section>

  <section class="hero" role="img" aria-label="Darkened photo of young readers at a book signing table"></section>
  <h2 class="hero-title">CHANGE A LIFE TODAY</h2>
  <div class="hero-rule"></div>
  <p class="hero-text">Sed eleifend turpis id hendrerit gravida. Etiam vitae ante auctor metus tristique porta.</p>
  <div class="buy-button">BUY NOW</div>

  <div class="brand-bar"><span class="brand-name">Lorna Quibb</span></div>

  <footer class="site-footer">
    <p class="copyright">© 2017 LORNA QUIBB &nbsp;&nbsp;|&nbsp;&nbsp; ALL RIGHTS RESERVED</p>
    <div class="social-links"><span></span><span></span><span></span></div>
  </footer>

  <div class="back-to-top">
    <svg width="14" height="9" viewBox="0 0 14 9"><path d="M2 7.5 L7 2.5 L12 7.5" fill="none" stroke="#ffffff" stroke-width="2"/></svg>
  </div>
</body>
</html>
```